Trifold Brochure needed for Hearthline Counseling

Hi! We need to have a trifold brochure made.

We would like to see brochure designs that use our logo colors, which are khaki, chocolate brown, and gray.

The brochure should be a modern design and please use your creativity.

Brochure is a trifold brochure, size is 8.5 x 11 and full color.

The following attachment has the content to be used in the trifold brochure, as well as some possible pictures. I have also attached our logo.

We would like to use file #2 for sure (picture number 31759204) and add the quote from her...

"At first, I was reluctant about going to Hearthline. Once I got there, I was glad I went. I learned a lot and was treated like family the whole time." Marlene Oakes

Requirements
Must have
• Our logo
• Information should be listed exactly as the attached document
• You must stick with our logo colors

```html
<!DOCTYPE html>
<html lang="en">
<head>
<meta charset="utf-8">
<title>Hearthline Counseling – Trifold Brochure</title>
<link rel="stylesheet" href="https://fonts.googleapis.com/css2?family=Vollkorn:wght@400;600;700&family=Source+Sans+3:wght@400;700&display=swap">
<style>
  :root {
    --gray: #87888b;
    --gray-dark: #77787b;
    --brown: #6a4a2b;
    --brown-deep: #5f4524;
    --khaki: #e3d3ac;
    --cream: #f7eedf;
    --cream-deep: #efe1c8;
    --white: #ffffff;
    --ink: #3b2a1a;
  }
  * { margin: 0; padding: 0; box-sizing: border-box; }
  html, body { width: 1200px; height: 934px; overflow: hidden; background: #fff; }
  .brochure {
    position: relative; width: 1200px; height: 934px; overflow: hidden;
    font-family: "Vollkorn", Georgia, serif;
  }
  .panel { position: absolute; top: 0; height: 934px; }

  /* FAQ panel */
  .faq { left: 0; width: 395px; background: var(--gray); color: var(--white); }
  .faq-header {
    position: absolute; top: 31px; left: 0; width: 395px; height: 113px;
    background: var(--white); display: flex; align-items: center; padding-left: 36px;
  }
  .faq-header .mark { width: 30px; height: 30px; border-radius: 50%; background: var(--gray); margin-right: 18px; }
  .faq-header h2 {
    color: var(--brown); font-weight: 600; font-size: 24px; line-height: 30px; letter-spacing: 0.3px;
  }
  .faq-list { position: absolute; top: 169px; left: 27px; width: 350px; }
  .faq-item { margin-bottom: 21px; }
  .faq-item h3 { color: var(--khaki); font-weight: 600; font-size: 17.5px; line-height: 22px; }
  .faq-item p { font-size: 17.5px; line-height: 22px; }
  .faq-item small { display: block; font-size: 13.5px; line-height: 17px; }

  /* Reminder panel */
  .reminders {
    left: 395px; width: 402px; text-align: center; color: var(--brown);
    background: linear-gradient(135deg, var(--cream) 0%, var(--cream-deep) 55%, var(--cream) 100%);
  }
  .reminders h1 { margin-top: 48px; font-size: 38.5px; line-height: 45px; font-weight: 700; }
  .reminders .note { margin: 0 auto 14px; width: 300px; font-size: 21px; line-height: 26px; }
  .reminders .note b { font-weight: 600; }
  .reminders .first { margin-top: 30px; }
  .contact-pill {
    position: absolute; top: 640px; left: 64px; width: 271px; height: 37px; border-radius: 19px;
    background: var(--gray); color: var(--white); font-size: 26px; font-weight: 700; line-height: 37px;
  }
  .phone { position: absolute; top: 684px; left: 0; width: 402px; font-size: 44px; font-weight: 700; color: var(--gray); }
  .email { position: absolute; top: 734px; left: 0; width: 402px; font-size: 18px; font-weight: 600; color: var(--gray); }
  .mission {
    position: absolute; top: 800px; left: 32px; width: 345px; text-align: left;
    font-family: "Source Sans 3", Arial, sans-serif; font-size: 14.7px; line-height: 21px; color: var(--ink);
  }
  .mission b { color: var(--brown); }

  /* Cover panel */
  .cover { left: 797px; width: 403px; background: linear-gradient(160deg, var(--cream) 0%, var(--cream-deep) 100%); }
  .cover-band { position: absolute; top: 0; left: 0; width: 403px; height: 165px; background: var(--gray); }
  .tagline {
    position: absolute; top: 45px; left: 36px; color: var(--white); font-size: 36px; line-height: 40px;
  }
  .tagline .line2 { display: block; padding-left: 33px; }
  .badge {
    position: absolute; top: 33px; left: 310px; width: 66px; height: 66px; border-radius: 50%;
    background: var(--khaki); color: var(--white); font-size: 44px; font-style: italic;
    text-align: center; line-height: 66px;
  }
  .photo { position: absolute; top: 165px; left: 0; width: 403px; height: 470px; }
  .logo-type { position: absolute; top: 745px; left: 0; width: 403px; text-align: right; padding-right: 30px; }
  .logo-type .name { display: flex; justify-content: flex-end; align-items: center; gap: 14px; color: var(--gray-dark); font-size: 56px; line-height: 60px; }
  .logo-type .dot { width: 26px; height: 26px; border-radius: 50%; background: var(--brown); }
  .logo-type .sub { font-family: "Source Sans 3", Arial, sans-serif; font-size: 14.5px; letter-spacing: 1px; color: var(--ink); margin-top: 8px; }
</style>
</head>
<body>
<main class="brochure">

  <section class="panel faq">
    <header class="faq-header">
      <span class="mark"></span>
      <h2>FREQUENTLY<br>ASKED QUESTIONS</h2>
    </header>
    <div class="faq-list">
      <div class="faq-item">
        <h3>What can I expect at<br>my appointment?</h3>
        <p>You can Expect to be treated like family throughout the entire visit. We will Respect your time and are dedicated to helping you better understand proactive opioid education.</p>
      </div>
      <div class="faq-item">
        <h3>How long will my appointment last?</h3>
        <p>Please allow 45 minutes to<br>complete your visit.</p>
        <small>(this allows time to complete your paperwork)</small>
      </div>
      <div class="faq-item">
        <h3>Will my information be<br>kept confidential?</h3>
        <p>Yes, your visit will only be shared with your referring doctor. Hearthline Counseling is HIPAA Compliant.</p>
      </div>
      <div class="faq-item">
        <h3>Why do you need my ID<br>&nbsp;and Insurance Card?</h3>
        <p>Your ID and insurance card are needed for verification and any labs tests that may be requested.</p>
      </div>
      <div class="faq-item">
        <h3>How much is my visit?</h3>
        <p>The office visit is only $40.</p>
        <small>( we have a hardship program for those in need)</small>
      </div>
      <div class="faq-item">
        <h3>Is this visit a one time appointment?</h3>
        <p>Hearthline sees patients 3 to 4 times a year Providing New Educational material and tools each time.</p>
        <small>(too much information for 1 visit)</small>
      </div>
    </div>
  </section>

  <section class="panel reminders">
    <h1>Appointment<br>Reminders</h1>
    <p class="note first"><b>Please bring Picture ID and Insurance Card (s)</b></p>
    <p class="note"><b>Please allow us up to 45 mins of your time to give you the best possible experience.</b></p>
    <p class="note"><b>Our office visit is only $40.</b><br>We accept credit, your check or cash.</p>
    <p class="note"><b>We are anxious to see You!</b><br>Please do not miss your appointment,<br>a 25.00 no show fee will be applied.</p>
    <div class="contact-pill">Contact us at</div>
    <div class="phone">555.214.0377</div>
    <div class="email">info@hearthlinecounseling.com</div>
    <p class="mission"><b>Hearthline</b> is a stepping stone for Future Success, and Your Future Success should be determined by how much You impact Your community. <b>Therefore, let's work Together in Making Solutions, One Patient at a time.</b></p>
  </section>

  <section class="panel cover">
    <div class="cover-band">
      <p class="tagline">Making Solutions<span class="line2">Patient at a Time</span></p>
      <div class="badge">1</div>
    </div>
    <svg class="photo" viewBox="0 0 403 470" role="img" aria-label="Photo of a smiling senior couple outdoors in front of green foliage">
      <defs>
        <linearGradient id="photoTone" x1="0" y1="0" x2="1" y2="1">
          <stop offset="0" stop-color="#7d9a4a"/>
          <stop offset="0.5" stop-color="#c9c2b4"/>
          <stop offset="1" stop-color="#3f7fc4"/>
        </linearGradient>
      </defs>
      <polygon points="0,0 403,0 403,370 145,455 0,420" fill="url(#photoTone)"/>
      <polygon points="145,455 403,370 403,510" fill="var(--brown-deep)"/>
    </svg>
    <div class="logo-type">
      <div class="name"><span class="dot"></span>Hearthline</div>
      <p class="sub">a pro-active opioid education center</p>
    </div>
  </section>

</main>
</body>
</html>
```